Business Card Design

We are a new residential construction company.our team is made up of young highly skilled tradesman of the next generation of carpenters coming through with new skills and ideas.we chose the name meridian as it means strikingly different from the rest as this is what we plan to be and we would like to portray this in our business card.we like Bold lettering as we want to make a statement, also the use of colour would be great as we want to stand out from the usual plain construction cards and logos.
I have attached a logo sketch I did as a rough idea if you can tidy it up or improve on it would be good.
I have also attached the LBP logo please include this on the card small but still legible.
open to any colourschemes ideas.
thanks
(note)please delete the LBP#308617 off from the card details please.
Updates
Industry/Entity Type
Construction
Contact Information for Business Card
MERIDIAN CONSTRUCTION LIMITED
Director:Kai Pereira
Mobile :0217364801
Email:Meridian.Construction@examplemail.test
Address:48 Halvorsen place,Ashgrove park 2071,Auckland
LBP#BP308617
Look and feel
Each slider illustrates characteristics of the customer's brand and the style your logo design should communicate.

```html
<!DOCTYPE html>
<html lang="en">
<head>
<meta charset="utf-8">
<title>Meridian Construction – Business Card</title>
<link href="https://fonts.googleapis.com/css2?family=IM+Fell+English&display=swap" rel="stylesheet">
<style>
  :root {
    --backdrop: #d9d9d7;
    --card-top: #ffffff;
    --card-mid: #cfe8c2;
    --card-bottom: #52b035;
    --brand-green: #4aa82c;
    --emblem-green: #a9d796;
    --text-light: #ffffff;
    --icon-dark: #1f2a1a;
  }
  html, body {
    margin: 0;
    width: 1200px;
    height: 1200px;
    overflow: hidden;
    background: var(--backdrop);
  }
  .card {
    position: absolute;
    left: 75px;
    top: 300px;
    width: 1050px;
    height: 600px;
    overflow: hidden;
    background: linear-gradient(to bottom, var(--card-top) 0%, var(--card-top) 12%, var(--card-mid) 45%, var(--card-bottom) 100%);
    box-shadow: 0 6px 18px rgba(0,0,0,0.18);
    font-family: "IM Fell English", Georgia, serif;
  }
  .brand-emblem {
    position: absolute;
    left: 70px;
    top: 40px;
    width: 150px;
    height: 150px;
    border-radius: 50%;
    background: var(--emblem-green);
  }
  .brand-name {
    position: absolute;
    color: var(--brand-green);
    margin: 0;
    font-weight: 400;
    line-height: 1;
    letter-spacing: 0.04em;
    white-space: nowrap;
  }
  .brand-name--primary { left: 300px; top: 105px; font-size: 96px; }
  .brand-name--secondary { left: 260px; top: 205px; font-size: 62px; }
  .contact-list {
    position: absolute;
    left: 60px;
    top: 370px;
    margin: 0;
    padding: 0;
    list-style: none;
    color: var(--text-light);
    font-size: 28px;
  }
  .contact-item {
    display: flex;
    align-items: center;
    gap: 18px;
    height: 46px;
    white-space: nowrap;
  }
  .contact-icon { width: 24px; height: 24px; flex: none; }
  .address {
    position: absolute;
    left: 640px;
    top: 470px;
    width: 380px;
    margin: 0;
    color: var(--text-light);
    text-align: center;
    font-size: 24px;
    line-height: 1.3;
    white-space: nowrap;
  }
  .address-label { font-size: 18px; letter-spacing: 0.12em; display: block; margin-bottom: 4px; }
</style>
</head>
<body>
  <section class="card" aria-label="Meridian Construction business card">
    <div class="brand-emblem" aria-hidden="true"></div>
    <p class="brand-name brand-name--primary">MERIDIAN</p>
    <p class="brand-name brand-name--secondary">CONSTRUCTION</p>

    <ul class="contact-list">
      <li class="contact-item">
        <svg class="contact-icon" viewBox="0 0 24 24" aria-hidden="true"><rect x="4" y="4" width="16" height="16" rx="3" fill="var(--icon-dark)"/></svg>
        <span>Kai Pereira</span>
      </li>
      <li class="contact-item">
        <svg class="contact-icon" viewBox="0 0 24 24" aria-hidden="true"><rect x="6" y="2" width="12" height="20" rx="2" fill="none" stroke="var(--icon-dark)" stroke-width="2"/><rect x="8" y="5" width="8" height="9" fill="var(--icon-dark)"/></svg>
        <span>0217364801</span>
      </li>
      <li class="contact-item">
        <svg class="contact-icon" viewBox="0 0 24 24" aria-hidden="true"><rect x="2" y="6" width="20" height="13" fill="var(--icon-dark)"/><path d="M2 6 L12 14 L22 6" fill="none" stroke="#3a4a33" stroke-width="1.5"/></svg>
        <span>meridian.construction@examplemail.test</span>
      </li>
    </ul>

    <p class="address">
      <span class="address-label">ADDRESS</span>
      48 Halvorsen place, Ashgrove park<br>
      2071, Auckland
    </p>
  </section>
</body>
</html>
```